Zia Lotte's Sweet Kitchen

I would like a website to tell the story of our cookies as well as products to sell. We make Pizzelle's from our Great Grandmothers cookie recipe. Our original product is Vanilla Pizzelle's but we have added other flavors as well as products. These are an italian Tradition and would like the logo be represented in the design

Target Market(s)

Dessert Lovers, Coffee/Tea drinkers, Italians, gifts

Industry/Entity Type

Baked goods, cookies

Coding

Colors
59FF00
82FF00
B8FF75
E3FFCB
F4FFEA
F0912C
F2A743
F7CA91
FBE8D2
FDF5EE
EB3D1F
EC4F4E
F09395
F8D3D4
FCEDEE

Requirements
Must have
• My logo, About Page, Products, ordering page
Nice to have
• I have uploaded my logo and Product labels so you can get an idea of colors and fonts

```html
<!DOCTYPE html>
<html lang="en">
<head>
<meta charset="utf-8">
<title>Zia Lotte's Sweet Kitchen</title>
<link rel="stylesheet" href="https://fonts.googleapis.com/css2?family=Inter:wght@400;500;600;700&family=Pinyon+Script&display=swap">
<style>
:root{
  --orange:#E8732A;
  --orange-soft:#F0912C;
  --ink:#1d1d1d;
  --muted:#6b6b6b;
  --grey-line:#b9b9b9;
  --panel:#eef0f3;
  --white:#ffffff;
  --footer:#000000;
  --blue:#2b8fd6;
}
*{box-sizing:border-box;margin:0;padding:0}
html,body{width:1200px;height:4601px;overflow:hidden}
body{position:relative;font-family:"Inter",Arial,sans-serif;color:var(--ink);background:var(--white)}
.abs{position:absolute}
.script{font-family:"Pinyon Script",cursive;font-weight:400;color:var(--ink);text-align:center;width:100%}

/* hero */
.hero{left:0;top:0;width:1200px;height:764px;background:radial-gradient(ellipse 520px 220px at 600px 300px,#e9b95a 0%,#d9a64e 40%,rgba(200,190,180,0) 100%),linear-gradient(180deg,#aeb3bd 0%,#bdb9b2 50%,#a9a39c 100%)}
.nav{left:86px;top:79px;width:1027px;height:76px;background:var(--white);border-radius:38px;box-shadow:0 4px 14px rgba(0,0,0,.12)}
.nav a{position:absolute;top:27px;font-size:15px;font-weight:500;color:var(--ink);text-decoration:none}
.nav a.active{color:var(--orange)}
.brand-badge{left:520px;top:32px;width:160px;height:160px;border-radius:50%;background:var(--white);box-shadow:0 4px 14px rgba(0,0,0,.12);display:flex;align-items:center;justify-content:center;text-align:center;color:var(--orange);font-weight:600;font-size:17px;line-height:1.25}
.phone-ico{left:744px;top:92px;width:50px;height:50px;border-radius:50%;border:1px solid #ddd;display:flex;align-items:center;justify-content:center}
.phone-num{left:808px;top:105px;font-size:17px;font-weight:600}
.order-btn{left:973px;top:79px;width:140px;height:76px;background:var(--orange);border-radius:0 38px 38px 0;color:var(--white);font-weight:600;font-size:16px;display:flex;align-items:center;justify-content:center}
.hero-title{top:455px;font-size:112px;color:var(--white);text-shadow:0 2px 8px rgba(0,0,0,.25)}
.hero-sub{top:610px;width:100%;text-align:center;color:var(--white);font-size:31px;font-weight:500;text-shadow:0 2px 6px rgba(0,0,0,.25)}
.dots{left:558px;top:697px;width:84px;height:28px;background:var(--white);border-radius:14px;display:flex;gap:12px;align-items:center;justify-content:center}
.dots i{width:9px;height:9px;border-radius:50%;background:#aaa}
.dots i.on{background:var(--orange)}

/* about */
.section-title{font-size:72px}
.about-lead{left:180px;top:1062px;width:840px;text-align:center;font-size:16px;line-height:32.5px;color:var(--muted)}
.about-photo{left:110px;top:1288px;width:368px;height:368px;border-radius:50%;background:radial-gradient(circle at 50% 40%,#b8262a 0%,#8c2a22 25%,#c49a6a 45%,#eeeeee 60%,#f4f4f4 100%)}
.about-copy{left:582px;top:1248px;width:520px;font-size:16px;line-height:32.5px;color:var(--muted)}
.about-copy p{margin-bottom:32px}
.btn{display:flex;align-items:center;justify-content:center;gap:10px;border-radius:27px;font-weight:600;font-size:16px}
.btn-solid{background:var(--orange);color:var(--white);box-shadow:0 6px 14px rgba(232,115,42,.3)}
.btn-outline{background:var(--white);color:var(--orange);border:2px solid var(--orange);box-shadow:0 6px 14px rgba(232,115,42,.2)}

/* products */
.products{left:0;top:1795px;width:1200px;height:836px;background:linear-gradient(180deg,#e9ebef 0%,#f1f1f1 80%,#e7d9d3 100%)}
.card{top:2027px;width:325px;height:502px;background:var(--white);border-radius:10px;box-shadow:0 6px 20px rgba(0,0,0,.06)}
.card-photo{position:absolute;left:9px;top:9px;width:307px;height:202px;border-radius:6px}
.card-label{position:absolute;left:98px;top:141px;width:128px;height:128px;border-radius:50%;background:radial-gradient(circle,#f4efe6 0 30%,#2f4a44 31% 70%,#7a4a2c 71%)}
.card h3{position:absolute;top:298px;width:100%;text-align:center;font-size:21px;font-weight:600}
.card .sub{position:absolute;top:336px;width:100%;text-align:center;font-size:17px;color:var(--muted)}
.card .net{position:absolute;top:370px;width:100%;text-align:center;font-size:15px;font-weight:700;color:var(--blue)}
.card .btn{position:absolute;left:78px;top:418px;width:168px;height:54px}

/* advantage */
.adv-title{top:2872px}
.adv-item{top:3138px;width:300px;text-align:center}
.adv-item h4{font-size:22px;font-weight:600;margin-bottom:12px}
.adv-item p{font-size:16px;line-height:33px;color:var(--muted)}

/* contact */
.contact{left:0;top:3415px;width:1200px;height:693px;background:radial-gradient(ellipse 500px 300px at 300px 700px,#5a2d18 0%,rgba(90,45,24,0) 100%),radial-gradient(ellipse 500px 300px at 900px 650px,#6a3018 0%,rgba(106,48,24,0) 100%),linear-gradient(180deg,#d8662c 0%,#e0703a 50%,#c85c28 100%)}
.contact-title{top:3490px;color:var(--white)}
.field{background:var(--white);border-radius:4px;display:flex;align-items:center;gap:14px;padding-left:28px;font-size:16px;color:#666}
.field.area{align-items:flex-start;padding-top:20px}

/* footer */
.footer{left:0;top:4108px;width:1200px;height:493px;background:var(--footer);color:var(--white)}
.footer h5{position:absolute;font-size:18px;font-weight:700}
.foot-brand{left:86px;top:4260px;width:128px;height:128px;border-radius:50%;border:2px solid var(--orange);display:flex;align-items:center;justify-content:center;text-align:center;color:var(--orange);font-weight:600;font-size:16px;line-height:1.3}
.links a{position:absolute;left:334px;font-size:17px;color:var(--white);text-decoration:none}
.chev{position:absolute;left:286px;color:var(--orange);font-size:18px;font-weight:700}
.ci{position:absolute;left:566px;font-size:17px;line-height:30px}
.news{left:818px;top:4268px;width:295px;height:52px;border-radius:26px;background:var(--white);border:2px solid var(--orange);color:#666;font-size:15px;padding-left:24px;display:flex;align-items:center}
.news-go{left:1062px;top:4273px;width:42px;height:42px;border-radius:50%;background:var(--orange)}
.social{top:4352px;width:50px;height:50px;border-radius:50%;border:2px solid var(--white)}
.rule{left:86px;top:4531px;width:1027px;height:1px;background:#2a2a2a}
.copy{left:0;top:4555px;width:1200px;text-align:center;font-size:15px;color:#777}
</style>
</head>
<body>

<!-- HERO -->
<div class="abs hero" role="img" aria-label="Stack of golden pizzelle cookies dusted with sugar on a cake stand"></div>
<nav class="abs nav">
  <a class="active" style="left:41px">Home</a>
  <a style="left:141px">About Us</a>
  <a style="left:267px">Our Products</a>
</nav>
<div class="abs brand-badge">Zia Lotte's<br>Sweet Kitchen</div>
<div class="abs phone-ico">
  <svg width="20" height="20" viewBox="0 0 24 24"><path fill="#E8732A" d="M6.6 10.8a15.1 15.1 0 0 0 6.6 6.6l2.2-2.2c.3-.3.7-.4 1-.2 1.1.4 2.3.6 3.6.6.6 0 1 .4 1 1V20c0 .6-.4 1-1 1A17 17 0 0 1 3 4c0-.6.4-1 1-1h3.5c.6 0 1 .4 1 1 0 1.3.2 2.5.6 3.6.1.3 0 .7-.2 1z"/></svg>
</div>
<div class="abs phone-num">555-014-2277</div>
<div class="abs order-btn">Order Now</div>
<h1 class="abs script hero-title">We make Pizzelle's</h1>
<p class="abs hero-sub">from our Great Grandmothers cookie recipe.</p>
<div class="abs dots"><i></i><i class="on"></i><i></i></div>

<!-- ABOUT -->
<h2 class="abs script section-title" style="top:955px">About Us</h2>
<p class="abs about-lead">Lorem ipsum dolor sit amet consectetur adipisicing elit, sed do eiusmod tempor incididunt ut labore et dolore magna aliqua. Ut enim ad minim veniam, quis nostrud exercitation ullamco laboris nisi ut aliquip ex ea commodo consequat. Duis aute irure dolor in reprehenderit in voluptate velit esse cillum dolore eu fugiat nulla pariaturx cepteur sint occaecat cupidatat non proident, sunt in culpa.</p>
<svg class="abs" style="left:80px;top:1262px" width="430" height="430" viewBox="0 0 430 430">
  <path d="M 215 10 A 205 205 0 1 0 360 360" fill="none" stroke="#b9b9b9" stroke-width="5"/>
  <path d="M 230 12 A 205 205 0 0 1 340 375" fill="none" stroke="#E8732A" stroke-width="5"/>
</svg>
<div class="abs about-photo" role="img" aria-label="Strawberries in a pizzelle cup on a white stand with chocolate chips"></div>
<div class="abs about-copy">
  <p>Eaque ipsa quae ab illo inventore veritatis et quasi architectos beatae vitae dicta sunt explicabo. Nemo enim ipsam volupisto tatem quia voluptas sit aspernatur aut odit aut fugit sed</p>
  <p>Consequuntur magni dolores eos qui ratione voluptatem sequi nesciunt. Neque porro quisquam est, qui dolorem ipsum quia dolor sit amet, consectetur, adipisci velit sed quia.</p>
  <p>Beatae vitae dicta sunt explicabo. Nemo enim ipsam voluptatas em quia voluptas sit aspernatur aut odit aut fugit sed quia cons seutur magni dolores eos qui ratione voluptatem sequi.</p>
</div>
<div class="abs btn btn-solid" style="left:582px;top:1637px;width:209px;height:54px">More About Us
  <svg width="18" height="18" viewBox="0 0 24 24"><circle cx="12" cy="12" r="10" fill="none" stroke="#fff" stroke-width="2"/><path d="M8 12h8M13 8l4 4-4 4" fill="none" stroke="#fff" stroke-width="2"/></svg>
</div>

<!-- PRODUCTS -->
<div class="abs products" role="img" aria-label="Light textured backdrop with scattered cocoa crumbs"></div>
<h2 class="abs script section-title" style="top:1880px">Our Products</h2>

<div class="abs card" style="left:86px">
  <div class="card-photo" style="background:linear-gradient(160deg,#e6e2de 0%,#c99b6e 45%,#a8764a 100%)" role="img" aria-label="Sugar dusted pizzelle with chocolate chips"></div>
  <div class="card-label" role="img" aria-label="Chai pizzelle product label"></div>
  <h3>Pizzelle's</h3><p class="sub">Italian waffle cookies</p><p class="net">NET WT. 3OZ</p>
  <div class="btn btn-outline">Order Now <svg width="16" height="16" viewBox="0 0 24 24"><circle cx="12" cy="12" r="10" fill="none" stroke="#E8732A" stroke-width="2"/><path d="M8 12h8M13 8l4 4-4 4" fill="none" stroke="#E8732A" stroke-width="2"/></svg></div>
</div>
<div class="abs card" style="left:437px">
  <div class="card-photo" style="background:linear-gradient(160deg,#e8e8e8 0%,#b98252 45%,#e2b24f 100%)" role="img" aria-label="Rolled pizzelle cones in chocolate and vanilla"></div>
  <div class="card-label" role="img" aria-label="Chocolate pizzelle product label"></div>
  <h3>Pizzelle's</h3><p class="sub">Italian waffle cookies</p><p class="net">NET WT. 3OZ</p>
  <div class="btn btn-solid">Order Now <svg width="16" height="16" viewBox="0 0 24 24"><circle cx="12" cy="12" r="10" fill="none" stroke="#fff" stroke-width="2"/><path d="M8 12h8M13 8l4 4-4 4" fill="none" stroke="#fff" stroke-width="2"/></svg></div>
</div>
<div class="abs card" style="left:788px">
  <div class="card-photo" style="background:linear-gradient(180deg,#c9cbcf 0%,#e3bd6a 50%,#bfc1c4 100%)" role="img" aria-label="Stack of vanilla pizzelle on a cake stand"></div>
  <div class="card-label" role="img" aria-label="Chai pizzelle product label"></div>
  <h3>Pizzelle's</h3><p class="sub">Italian waffle cookies</p><p class="net">NET WT. 3OZ</p>
  <div class="btn btn-outline">Order Now <svg width="16" height="16" viewBox="0 0 24 24"><circle cx="12" cy="12" r="10" fill="none" stroke="#E8732A" stroke-width="2"/><path d="M8 12h8M13 8l4 4-4 4" fill="none" stroke="#E8732A" stroke-width="2"/></svg></div>
</div>

<!-- ADVANTAGE -->
<h2 class="abs script section-title adv-title">Our Advantage</h2>
<svg class="abs" style="left:0;top:2950px" width="1200" height="380" viewBox="0 2950 1200 380">
  <path d="M 353 3033 A 154 154 0 1 0 368 3246 C 420 3190 440 3080 492 3029 A 154 154 0 0 1 709 3048" fill="none" stroke="#E8732A" stroke-width="5"/>
  <circle cx="353" cy="3033" r="10" fill="#E8732A"/>
  <circle cx="709" cy="3048" r="10" fill="#E8732A"/>
  <path d="M 458 3224 A 154 154 0 0 0 709 3246 C 760 3180 770 3090 820 3048 A 154 154 0 1 1 839 3265" fill="none" stroke="#b9b9b9" stroke-width="5"/>
  <circle cx="458" cy="3224" r="10" fill="#b9b9b9"/>
  <circle cx="839" cy="3265" r="10" fill="#b9b9b9"/>
  <!-- oven icon -->
  <g fill="none" stroke="#aaa" stroke-width="2">
    <rect x="216" y="3068" width="70" height="44" rx="4"/><rect x="224" y="3076" width="42" height="28"/><path d="M276 3080h4M276 3090h4M276 3100h4M244 3058q7-6 14 0"/>
  </g>
  <!-- rolling pin icon -->
  <g fill="none" stroke="#aaa" stroke-width="2">
    <circle cx="591" cy="3084" r="28"/><path d="M571 3104l40-40M577 3098l-6 6M605 3070l6-6"/>
  </g>
  <!-- pie icon -->
  <g fill="none" stroke="#aaa" stroke-width="2">
    <circle cx="938" cy="3084" r="28" stroke-dasharray="4 3"/><circle cx="938" cy="3084" r="18"/>
  </g>
</svg>
<div class="abs adv-item" style="left:100px"><h4>Fresh Baked</h4><p>Lorem ipsum dolor sit ametos<br>consectetur adipiscing.</p></div>
<div class="abs adv-item" style="left:441px"><h4>Original Product</h4><p>Lorem ipsum dolor sit ametos<br>consectetur adipiscing.</p></div>
<div class="abs adv-item" style="left:788px"><h4>Many Flavors</h4><p>Lorem ipsum dolor sit ametos<br>consectetur adipiscing.</p></div>

<!-- CONTACT -->
<div class="abs contact" role="img" aria-label="Orange tinted backdrop of cocoa dust and chocolate chips"></div>
<h2 class="abs script section-title contact-title">Contact Us</h2>
<div class="abs field" style="left:130px;top:3645px;width:302px;height:54px"><svg width="16" height="16" viewBox="0 0 24 24"><circle cx="12" cy="7" r="5" fill="#666"/><path d="M2 22c0-6 5-9 10-9s10 3 10 9z" fill="#666"/></svg>Full Name</div>
<div class="abs field" style="left:450px;top:3645px;width:300px;height:54px"><svg width="16" height="16" viewBox="0 0 24 24"><path fill="#666" d="M6.6 10.8a15.1 15.1 0 0 0 6.6 6.6l2.2-2.2c.3-.3.7-.4 1-.2 1.1.4 2.3.6 3.6.6.6 0 1 .4 1 1V20c0 .6-.4 1-1 1A17 17 0 0 1 3 4c0-.6.4-1 1-1h3.5c.6 0 1 .4 1 1 0 1.3.2 2.5.6 3.6.1.3 0 .7-.2 1z"/></svg>Phone No</div>
<div class="abs field" style="left:768px;top:3645px;width:300px;height:54px"><svg width="16" height="16" viewBox="0 0 24 24"><rect x="2" y="5" width="20" height="14" rx="2" fill="#666"/><path d="M2 6l10 7 10-7" fill="none" stroke="#fff" stroke-width="2"/></svg>Email Address</div>
<div class="abs field area" style="left:130px;top:3716px;width:938px;height:215px"><svg width="16" height="16" viewBox="0 0 24 24"><path d="M3 3h18v13H8l-5 5z" fill="#666"/></svg>Write a Mesage</div>
<div class="abs btn btn-solid" style="left:518px;top:3952px;width:164px;height:54px">Send Now <svg width="16" height="16" viewBox="0 0 24 24"><circle cx="12" cy="12" r="10" fill="none" stroke="#fff" stroke-width="2"/><path d="M8 12h8M13 8l4 4-4 4" fill="none" stroke="#fff" stroke-width="2"/></svg></div>

<!-- FOOTER -->
<footer class="abs footer"></footer>
<div class="abs foot-brand">Zia Lotte's<br>Sweet Kitchen</div>
<h5 style="position:absolute;left:286px;top:4213px;color:#fff">Quick Links</h5>
<div class="links">
  <span class="chev" style="top:4260px">»</span><a style="top:4261px">Home</a>
  <span class="chev" style="top:4303px">»</span><a style="top:4304px">About Us</a>
  <span class="chev" style="top:4346px">»</span><a style="top:4347px">Our Products</a>
  <span class="chev" style="top:4389px">»</span><a style="top:4390px">Order Now</a>
</div>
<h5 style="position:absolute;left:514px;top:4213px;color:#fff">Contact Info</h5>
<svg class="abs" style="left:512px;top:4263px" width="16" height="20" viewBox="0 0 24 30"><path d="M12 0a10 10 0 0 0-10 10c0 8 10 20 10 20s10-12 10-20A10 10 0 0 0 12 0zm0 14a4 4 0 1 1 0-8 4 4 0 0 1 0 8z" fill="#E8732A"/></svg>
<div class="ci" style="top:4257px;color:#fff"><b>ADDRESS:</b></div>
<div class="ci" style="top:4293px;color:#fff">465, Loram ipsum dol<br>United States.</div>
<svg class="abs" style="left:512px;top:4374px" width="18" height="18" viewBox="0 0 24 24"><path fill="#E8732A" d="M6.6 10.8a15.1 15.1 0 0 0 6.6 6.6l2.2-2.2c.3-.3.7-.4 1-.2 1.1.4 2.3.6 3.6.6.6 0 1 .4 1 1V20c0 .6-.4 1-1 1A17 17 0 0 1 3 4c0-.6.4-1 1-1h3.5c.6 0 1 .4 1 1 0 1.3.2 2.5.6 3.6.1.3 0 .7-.2 1z"/></svg>
<div class="ci" style="top:4369px;color:#fff"><b>PHONE:</b></div>
<div class="ci" style="top:4405px;left:566px;color:#fff">555-014-2277</div>
<h5 style="position:absolute;left:818px;top:4213px;color:#fff">Join Newsletter</h5>
<div class="abs news">Email address</div>
<div class="abs news-go"><svg width="42" height="42" viewBox="0 0 42 42"><circle cx="21" cy="21" r="9" fill="none" stroke="#fff" stroke-width="2"/><path d="M17 21h8M22 17l4 4-4 4" fill="none" stroke="#fff" stroke-width="2"/></svg></div>
<div class="abs social" style="left:818px"></div>
<div class="abs social" style="left:877px"></div>
<div class="abs social" style="left:936px"></div>
<div class="abs rule"></div>
<p class="abs copy">Copyright © 2023 Zia Lotte's Sweet Kitchen. All rights reserved.</p>

</body>
</html>
```